Business Card for premium dental clinic

We are a premium dental clinic based in Brasov, Romania with more than 15 year on the market, providing quality dental treatment made by a team of more specialized dentists, working with modern equipment as a solution to beautiful and healthy teeth.

Our current logo for the clinic use 2 square with colors black and gold - dr Corbescu - studio, using family fonts Bodoni, Myriad Pro and Segoe Print.
Depending on the printing we used some gold CMYK background or gold foil picture background or a gold gradient.
We want a business card:
- eye catching business card
- distinguished business card
- premium design
- to keep the color scheme of black and gold
- to attract the customers to spent time reading the information
- modern concept

```html
<!DOCTYPE html>
<html lang="en">
<head>
<meta charset="utf-8">
<title>dr. Corbescu studio – business card</title>
<link rel="stylesheet" href="https://fonts.googleapis.com/css2?family=PT+Sans+Narrow:wght@400;700&family=Source+Sans+3:wght@400;600&display=swap">
<style>
  :root {
    --ink: #231f20;
    --paper: #ffffff;
    --gold: #e3b43c;
    --gold-light: #f4d872;
    --gold-deep: #b8861e;
    --name-gold: #c99a3e;
    --brand-font: "PT Sans Narrow", "Arial Narrow", sans-serif;
    --body-font: "Source Sans 3", "Myriad Pro", sans-serif;
  }
  * { box-sizing: border-box; margin: 0; padding: 0; }
  html, body { width: 1200px; height: 1200px; overflow: hidden; background: var(--paper); }
  .canvas { position: relative; width: 1200px; height: 1200px; }

  .gold-foil {
    background:
      radial-gradient(ellipse at 30% 25%, var(--gold-light) 0%, transparent 55%),
      radial-gradient(ellipse at 75% 80%, var(--gold-light) 0%, transparent 50%),
      linear-gradient(135deg, var(--gold) 0%, var(--gold-deep) 45%, var(--gold) 70%, var(--gold-deep) 100%);
  }

  /* Front */
  .card-front {
    position: absolute; left: 330px; top: 192px; width: 541px; height: 300px;
    background: var(--ink); overflow: hidden;
  }
  .front-strip { position: absolute; left: 0; top: 0; width: 34px; height: 100%; }
  .front-slash { position: absolute; left: 0; top: 66px; width: 34px; height: 30px; }

  .logo-box {
    position: absolute; left: 143px; top: 27px; width: 255px; height: 126px;
    border: 2px solid var(--paper); display: flex;
  }
  .logo-box .foil-half { width: 126px; height: 100%; position: relative; }
  .logo-box .dark-half { flex: 1; position: relative; }
  .name-plate {
    position: absolute; background: var(--paper); color: var(--ink);
    font-family: var(--brand-font); font-weight: 400; line-height: 1.05;
    display: flex; flex-direction: column; justify-content: center;
    white-space: nowrap;
  }
  .logo-box .name-plate { left: 16px; top: 42px; width: 110px; height: 42px; font-size: 16px; padding-left: 8px; }
  .tagline {
    position: absolute; right: 6px; color: var(--paper);
    font-family: var(--brand-font); font-weight: 700; line-height: 1; white-space: nowrap;
  }
  .logo-box .tagline { bottom: 6px; font-size: 13px; }

  .contact-list { position: absolute; left: 0; top: 178px; list-style: none; }
  .contact-list li { height: 26px; display: flex; align-items: center; }
  .contact-list .icon { width: 34px; display: flex; justify-content: center; }
  .contact-list .value {
    padding-left: 10px; color: var(--gold);
    font-family: var(--body-font); font-size: 21px; letter-spacing: 0.3px; line-height: 1;
  }

  .holder { position: absolute; left: 318px; top: 194px; width: 172px; text-align: center; }
  .holder .name {
    font-family: var(--body-font); font-weight: 600; font-size: 31px;
    color: var(--name-gold); line-height: 1; white-space: nowrap;
  }
  .holder .title {
    font-family: var(--body-font); font-size: 9px; letter-spacing: 5px;
    color: var(--name-gold); margin-top: 3px; padding-left: 5px;
  }

  /* Back */
  .card-back { position: absolute; left: 330px; top: 707px; width: 541px; height: 303px; }
  .rule { position: absolute; left: 0; width: 100%; background: var(--ink); }
  .rule.band-top { top: 0; height: 11px; }
  .rule.line-top { top: 15px; height: 3px; }
  .rule.line-bottom { top: 288px; height: 3px; }
  .rule.band-bottom { top: 292px; height: 11px; }
  .back-panel { position: absolute; top: 19px; left: 0; width: 100%; height: 266px; display: flex; }
  .back-panel .foil-half { width: 269px; height: 100%; position: relative; }
  .back-panel .dark-half { flex: 1; background: var(--ink); position: relative; }
  .back-panel .name-plate { left: 30px; top: 84px; width: 239px; height: 95px; font-size: 40px; padding-left: 18px; }
  .back-panel .tagline { right: 10px; bottom: 14px; font-size: 37px; font-weight: 400; }
</style>
</head>
<body>
<main class="canvas">

  <section class="card-front" aria-label="Business card front">
    <div class="front-strip gold-foil" role="img" aria-label="Gold foil texture"></div>
    <svg class="front-slash" viewBox="0 0 34 30" aria-hidden="true">
      <polygon points="0,22 34,0 34,9 0,30" fill="var(--ink)"/>
    </svg>

    <div class="logo-box">
      <div class="foil-half gold-foil" role="img" aria-label="Gold foil texture">
        <div class="name-plate"><span>dr. Corbescu</span><span>studio</span></div>
      </div>
      <div class="dark-half"><span class="tagline">dental clinic</span></div>
    </div>

    <ul class="contact-list">
      <li><span class="icon"><svg width="12" height="18" viewBox="0 0 12 18"><rect x="1" y="1" width="10" height="16" rx="1.5" fill="none" stroke="var(--ink)" stroke-width="1.6"/><rect x="3" y="3" width="6" height="10" fill="var(--ink)"/></svg></span><span class="value">+1234567890</span></li>
      <li><span class="icon"><svg width="16" height="16" viewBox="0 0 16 16"><path d="M4 1 L6.5 4.5 L5 6.5 Q6.5 10 9.5 11 L11.5 9.5 L15 12 L13 15 Q5 14 1 3 Z" fill="var(--ink)"/></svg></span><span class="value">+1234567890</span></li>
      <li><span class="icon"><svg width="17" height="12" viewBox="0 0 17 12"><rect x="0.5" y="0.5" width="16" height="11" fill="var(--ink)"/><path d="M1 1 L8.5 7 L16 1" fill="none" stroke="var(--gold)" stroke-width="1.2"/></svg></span><span class="value">yourmail@mail.com</span></li>
      <li><span class="icon"><svg width="16" height="16" viewBox="0 0 16 16" fill="none" stroke="var(--ink)" stroke-width="1.3"><circle cx="8" cy="8" r="7"/><ellipse cx="8" cy="8" rx="3" ry="7"/><path d="M1 8 H15 M2.5 4.5 H13.5 M2.5 11.5 H13.5"/></svg></span><span class="value">www.yoursite.com</span></li>
    </ul>

    <div class="holder">
      <p class="name">YourName</p>
      <p class="title">TITLE</p>
    </div>
  </section>

  <section class="card-back" aria-label="Business card back">
    <div class="rule band-top"></div>
    <div class="rule line-top"></div>
    <div class="back-panel">
      <div class="foil-half gold-foil" role="img" aria-label="Gold foil texture">
        <div class="name-plate"><span>dr. Corbescu</span><span>studio</span></div>
      </div>
      <div class="dark-half"><span class="tagline">dental clinic</span></div>
    </div>
    <div class="rule line-bottom"></div>
    <div class="rule band-bottom"></div>
  </section>

</main>
</body>
</html>
```